Meridian Handsets business card design

I would like to see some designs for a business card for Meridian Handsets. I would like the business card to be double sided. It will need to have a similar colour / look and feel to our website www.meridianhandsets.com.au I have also attached our latest flyer. Final designs to be handed over in Photoshop format so that I can edit the business card when needed please.

Industry/Entity Type

Business

Contact Information for Business Card

Gavin Thornley
sales@meridianhandsets.com.au
Business Development Manager
ph: (08) 6197 5821
www.meridianhandsets.com.au

Font styles to use
Serif
Sans Serif

Requirements
Must have
• If you could please utilise our colour scheme as seen on our website and the attached flyer.
• I would also like the final design to be in a Photoshop format so that I can edit it when needed please.

```html
<!DOCTYPE html>
<html lang="en">
<head>
<meta charset="utf-8">
<title>Meridian Handsets – Business Card</title>
<link rel="stylesheet" href="https://fonts.googleapis.com/css2?family=Open+Sans:wght@400;600;700&display=swap">
<style>
  :root {
    --brand-blue: #0a7fc0;
    --name-blue: #1b86c8;
    --charcoal: #333234;
    --ink: #2b2b2b;
    --paper: #ffffff;
    --backdrop: #e9e7e5;
    --text-light: #f2f2f2;
  }
  * { margin: 0; padding: 0; box-sizing: border-box; }
  html, body {
    width: 1200px; height: 900px; overflow: hidden;
    background: var(--backdrop);
    font-family: "Open Sans", Arial, sans-serif;
  }
  .card {
    position: absolute;
    background: var(--paper);
    box-shadow: 0 4px 14px rgba(0,0,0,0.18);
    overflow: hidden;
  }
  .card--front { left: 77px; top: 34px; width: 589px; height: 364px; }
  .card--back  { left: 388px; top: 505px; width: 567px; height: 352px; }

  .wordmark {
    font-family: "Open Sans", Arial, sans-serif;
    font-weight: 600;
    letter-spacing: -0.5px;
    white-space: nowrap;
  }
  .card--front .wordmark {
    position: absolute; left: 31px; top: 54px;
    font-size: 40px; color: var(--ink);
  }
  .contact-panel {
    position: absolute; left: 0; top: 155px; width: 100%; height: 209px;
    background: var(--charcoal);
    border-top: 3px solid #262527;
  }
  .person-name {
    position: absolute; left: 31px; top: 16px;
    font-size: 20px; font-weight: 600; color: var(--name-blue);
  }
  .person-role {
    position: absolute; left: 31px; top: 45px;
    font-size: 15px; color: var(--text-light);
  }
  .contact-list {
    position: absolute; left: 31px; top: 108px;
    list-style: none;
  }
  .contact-list li {
    display: flex; align-items: center; gap: 7px;
    height: 24.5px;
    font-size: 15px; color: var(--text-light);
  }
  .contact-list svg { width: 12px; height: 12px; fill: var(--name-blue); flex: none; }

  .brand-band {
    position: absolute; left: 0; top: 110px; width: 100%; height: 131px;
    background: var(--brand-blue);
    display: flex; align-items: center; justify-content: center;
  }
  .card--back .wordmark { font-size: 40px; color: var(--paper); }
</style>
</head>
<body>

<section class="card card--front" aria-label="Business card front">
  <div class="wordmark">Meridian Handsets</div>
  <div class="contact-panel">
    <h1 class="person-name">Gavin Thornley</h1>
    <p class="person-role">Business Development Manager</p>
    <ul class="contact-list">
      <li>
        <svg viewBox="0 0 24 24" aria-hidden="true"><path d="M6.6 10.8a15.2 15.2 0 0 0 6.6 6.6l2.2-2.2a1 1 0 0 1 1-.25 11.4 11.4 0 0 0 3.6.57 1 1 0 0 1 1 1V20a1 1 0 0 1-1 1A17 17 0 0 1 3 4a1 1 0 0 1 1-1h3.5a1 1 0 0 1 1 1c0 1.25.2 2.45.57 3.57a1 1 0 0 1-.25 1z"/></svg>
        (08) 6197 5821
      </li>
      <li>
        <svg viewBox="0 0 24 24" aria-hidden="true"><path d="M2 5h20v14H2z M3 6l9 7 9-7" /></svg>
        sales@meridianhandsets.com.au
      </li>
      <li>
        <svg viewBox="0 0 24 24" aria-hidden="true"><circle cx="12" cy="12" r="10"/></svg>
        www.meridianhandsets.com.au
      </li>
    </ul>
  </div>
</section>

<section class="card card--back" aria-label="Business card back">
  <div class="brand-band">
    <div class="wordmark">Meridian Handsets</div>
  </div>
</section>

</body>
</html>
```